Core Values Poster for Technology Business

A core values poster for our office. We don't have much in mind beyond a couple of logos (we have two companies) and then the 4 Core Values we want to present. Mostly, we want this to be simple (easy to take in as a reminder in 5-10 seconds) in a very visually appealing way.

If you can incorporate a high-look-and-feel, great, but not if it over complicates the entire poster/sign.

The core values are:
Relationships Matter
Passion Drives us to Excellence
All About Teamwork
Consistent, Resourceful, Relentless

Our file with both logos together is attached. This is a low-res version. We would provide a high-res version for final production.

Industry/Entity Type

Business

Font styles to use
Serif

Colors
ec1f27
0255a3

Requirements
Nice to have
• This is an update. To be able to incorporate some of our corporate look-and-feel, but not have a black background (as on our kovaline.com stie), please see the Video Conferencing Slick file that I have uploaded. Might be able to use parts of this type of format to tie in (but not use it exactly as-is - since this is a client facing document).

```html
<!DOCTYPE html>
<html lang="en">
<head>
<meta charset="utf-8">
<title>Core Values</title>
<link rel="stylesheet" href="https://fonts.googleapis.com/css2?family=Oswald:wght@500;600;700&display=swap">
<style>
  :root {
    --ink: #1d2a44;
    --paper: #ffffff;
    --night: #050608;
    --dusk: #3a3c40;
    --band-red: #e0365a;
    --ribbon-blue: #2c7fb2;
    --ribbon-dot: #f4ecaa;
    --text-light: #ffffff;
    --icon-fill: rgba(255, 255, 255, 0.82);
  }
  html, body {
    margin: 0;
    padding: 0;
    width: 800px;
    height: 1200px;
    overflow: hidden;
    background: var(--night);
  }
  .poster {
    position: relative;
    width: 800px;
    height: 1200px;
    overflow: hidden;
    font-family: "Oswald", "Arial Narrow", sans-serif;
    background: linear-gradient(180deg, var(--paper) 0px, var(--paper) 110px, #bfc0c2 170px, var(--dusk) 250px, #111215 340px, var(--night) 420px, var(--night) 100%);
  }
  .poster > * { position: absolute; }

  .brand {
    display: flex;
    align-items: center;
    gap: 10px;
    color: var(--ink);
    font-weight: 600;
    line-height: 1.05;
  }
  .brand-left { left: 30px; top: 40px; font-size: 26px; }
  .brand-left .brand-mark {
    width: 30px; height: 30px; border-radius: 50%;
    background: var(--band-red); flex: none;
  }
  .brand-right { right: 34px; top: 50px; font-size: 26px; }
  .brand-right .brand-mark {
    width: 24px; height: 24px; background: var(--ribbon-blue); flex: none;
  }

  .arch {
    left: 0; top: 0;
    width: 800px; height: 1200px;
  }
  .band-red { fill: var(--band-red); }
  .band-blue { fill: var(--ribbon-blue); }
  .ribbon-dot { fill: var(--ribbon-dot); }

  .headline {
    left: 0; width: 800px; top: 178px;
    margin: 0;
    text-align: center;
    color: var(--text-light);
    font-size: 74px;
    font-weight: 600;
    font-variant: small-caps;
    letter-spacing: 2px;
    line-height: 1;
    text-shadow: 0 3px 0 rgba(0, 0, 0, 0.45);
  }

  .value {
    margin: 0;
    color: var(--text-light);
    font-weight: 600;
    font-variant: small-caps;
    line-height: 1;
    white-space: nowrap;
  }
  .value-relationships { left: 207px; top: 408px; font-size: 66px; letter-spacing: 1px; }
  .value-passion { left: 66px; top: 496px; font-size: 72px; }
  .value-passion .line-2 { display: block; font-size: 84px; margin-top: 2px; text-transform: uppercase; font-variant: normal; }
  .value-teamwork { left: 278px; top: 688px; font-size: 104px; }
  .value-teamwork .line-2 { display: block; font-size: 98px; margin-top: -6px; padding-left: 8px; }
  .value-grit { left: 98px; top: 886px; font-size: 86px; }
  .value-grit .line-2 { display: block; font-size: 64px; margin-top: 2px; }
  .value-grit .line-3 { display: block; font-size: 80px; margin-top: 0; text-transform: uppercase; font-variant: normal; }

  .hearts-icon { left: 58px; top: 412px; width: 116px; height: 68px; }
  .icon-slot {
    background: radial-gradient(circle at 50% 50%, var(--icon-fill), rgba(255, 255, 255, 0.55));
    border-radius: 14px;
  }
  .handshake-icon { left: 588px; top: 507px; width: 172px; height: 118px; }
  .team-trophy-icon { left: 108px; top: 700px; width: 140px; height: 148px; }
  .process-icon { left: 488px; top: 906px; width: 226px; height: 180px; border-radius: 50%; }
</style>
</head>
<body>
<main class="poster">
  <div class="brand brand-left"><span class="brand-mark"></span><span>Orvane<br>Technology Solutions</span></div>
  <div class="brand brand-right"><span class="brand-mark"></span><span>Harbor Ridge Security Group</span></div>

  <svg class="arch" viewBox="0 0 600 900" preserveAspectRatio="none" aria-hidden="true">
    <path class="band-red" d="M0,125 Q300,45 600,125 L600,150 Q300,60 0,150 Z"/>
    <path class="band-blue" d="M0,152 Q300,78 600,152 L600,242 Q300,178 0,242 Z"/>
    <path class="band-red" d="M0,258 Q300,176 600,258 L600,298 Q300,196 0,298 Z"/>
    <circle class="ribbon-dot" cx="128" cy="190" r="7"/>
    <circle class="ribbon-dot" cx="472" cy="190" r="7"/>
  </svg>

  <h1 class="headline">Core Values</h1>

  <svg class="hearts-icon" viewBox="0 0 116 68" aria-hidden="true">
    <g fill="none" stroke="#ffffff" stroke-width="7" stroke-linejoin="round">
      <path d="M38,62 L10,34 A15,15 0 0 1 38,12 A15,15 0 0 1 66,34 Z"/>
      <path d="M78,62 L50,34 A15,15 0 0 1 78,12 A15,15 0 0 1 106,34 Z"/>
    </g>
  </svg>
  <p class="value value-relationships">Relationships Matter</p>

  <p class="value value-passion">Passion Drives us<span class="line-2">to Excellence</span></p>
  <div class="icon-slot handshake-icon" role="img" aria-label="White handshake icon"></div>

  <div class="icon-slot team-trophy-icon" role="img" aria-label="White icon of two teammates raising a trophy together"></div>
  <p class="value value-teamwork">All About<span class="line-2">teamwork</span></p>

  <p class="value value-grit">Consistent<span class="line-2">resourceful</span><span class="line-3">Relentless</span></p>
  <div class="icon-slot process-icon" role="img" aria-label="White linked circle icons showing a team, a rising chart and a gear"></div>
</main>
</body>
</html>
```